Performance Psychology Business Card Design + Letterhead

I require a new business card and letterhead for my consulting business. I am a psychologist working predominantly in sport psychology and organisational psychology. I consult to elite athletes and corporates.
I provide counselling services, workshops, assessments, and group sessions.
I'd like to use the colours in the logo.
My current card and letterhead is predominantly white - which I do like, but I'm up to try something different as well!
The letterhead doesn't need to have my name or title on it - but it can
The company is about success, achievement and reaching potential.
My website is at www.harvodel.com.au
I have changed some of my contact details, so I definitely need a new card and I would like this project to go ahead.
Thank you for putting the time into my design - I'm really excited about a new card and appreciate your contribution.
*IMPORTANT: The Fax Number Should be: 07 41 58 39 06
Target Market(s)
Elite athletes and teams
Corporate clients
Industry/Entity Type
Business
Contact Information for Business Card
Dr Marlise Quenby
Director (this is optional - I don't have to have this on there)
Level 2, 48 Wexbridge St
Townsville Qld 4810
M: 0431 562 047
F: 07 41 306 259
E: mq@harvodel.com.au
W: www.harvodel.com.au
Requirements
Must have
- Logo - I have one with a white background and one with blue - don't mind which one is used. Currently I have the white logo on letterhead and cards.
I would like to have the catchphrase of the company
... the best you can be
on the card somewhere.
Nice to have
- On my current card I have a few lines on the back to write appointment times for clients - however this isn't essential
I also have some of the key services provided:
- Performance Enhancement
- Assessment & Reports
- Individual & Group Counselling
- Executive coaching & Motivation
- Seminars & Workshops
I have a QR file - don't have it on my current card, but thinking it could go on the business card (probably not letterhead?). For some reason I can only load one file, so can send it through if it's needed.

```html
<!DOCTYPE html>
<html lang="en">
<head>
<meta charset="utf-8">
<title>Harvodel – Card Back</title>
<link rel="stylesheet" href="https://fonts.googleapis.com/css2?family=Gentium+Book+Plus:wght@700&family=Oswald:wght@700&display=swap">
<style>
  :root {
    --paper: #e2e5e8;
    --paper-dark: #d6dadd;
    --ink: #111111;
    --white: #ffffff;
    --photo-blue-light: #9fb8d2;
    --photo-slate: #7a7f86;
    --photo-warm: #8c7566;
    --photo-blue: #6f93bd;
  }
  * { margin: 0; padding: 0; box-sizing: border-box; }
  html, body { width: 1200px; height: 741px; overflow: hidden; background: var(--paper); }
  .card {
    position: relative;
    width: 1200px;
    height: 741px;
    background: linear-gradient(180deg, var(--paper) 0%, var(--paper-dark) 100%);
    overflow: hidden;
  }
  .hero-photo {
    position: absolute;
    left: 0; top: 0;
    width: 1200px; height: 527px;
    background: linear-gradient(90deg, var(--photo-blue-light) 0%, var(--photo-slate) 28%, var(--photo-warm) 52%, var(--photo-slate) 72%, var(--photo-blue) 88%, var(--photo-blue-light) 100%);
  }
  .tagline {
    position: absolute;
    left: 174px; top: 62px;
    width: 852px;
    text-align: center;
    font-family: "Oswald", "Arial Narrow", sans-serif;
    font-weight: 700;
    font-size: 112px;
    line-height: 1;
    letter-spacing: -2px;
    white-space: nowrap;
    color: rgba(255,255,255,0.55);
  }
  .services {
    position: absolute;
    left: 213px; top: 201px;
    list-style: none;
  }
  .services li {
    position: relative;
    padding-left: 66px;
    height: 55.5px;
    font-family: "Gentium Book Plus", "Palatino Linotype", serif;
    font-weight: 700;
    font-size: 48px;
    line-height: 55.5px;
    color: var(--white);
    text-shadow: 2px 2px 3px rgba(0,0,0,0.85);
    white-space: nowrap;
  }
  .services li::before {
    content: "";
    position: absolute;
    left: 0; top: 20px;
    width: 30px; height: 18px;
    border: 3px solid var(--white);
    box-shadow: 1px 1px 2px rgba(0,0,0,0.7);
  }
  .notes-box {
    position: absolute;
    left: 45px; top: 563px;
    width: 1108px; height: 127px;
    border: 3px solid var(--ink);
  }
  .notes-label {
    position: absolute;
    left: 21px; top: 12px;
    font-family: "Gentium Book Plus", "Palatino Linotype", serif;
    font-weight: 700;
    font-size: 30px;
    color: var(--ink);
  }
</style>
</head>
<body>
  <div class="card">
    <div class="hero-photo" role="img" aria-label="Photo of several hands cupped together holding soil with a small green seedling"></div>
    <div class="tagline">the best you can be</div>
    <ul class="services">
      <li>Performance Enhancement</li>
      <li>Assessment &amp; Reports</li>
      <li>Individual &amp; Group Counselling</li>
      <li>Executive coaching &amp; Motivation</li>
      <li>Seminars &amp; Workshops</li>
    </ul>
    <div class="notes-box">
      <span class="notes-label">Notes :</span>
    </div>
  </div>
</body>
</html>
```